Would like a website to blog, vlog and post pictures about a upcoming glowtrek road trip in a 1977 kd van.
We will have custom bumper stickers available (by donation or a set amount - unsure) and would like to be able mail these out in the future.
Would like the website to be easy to use, simple. clean with a modern hippie/boho feel.
The travelling van is original green. We have a custom lic plate 'glowtrek'
The stickers are black, white and red.
Our mission:
A Love movement journey to raise the vibration and awareness of Universal Love.
We plan to have it painted with washable paint at certain spots along the way. We will ask willing people to make a journal entry of how they glowtrek (spread the love) and I will quote them in my blog or blog.
The picture attached is me, Dorianne after we painted "Breezy" (the van's given name) with friends for a Canada Day celebration.
The road trip is with my boyfriend and our two 13yr olds - a boy and a girl.
However, the road trip in August is just the beginning of what I envision to be a much longer journey...so I would like the website created to hold space for future adventures :)
Happy creating to whomever feels their heart strings pulled to be part of our glowtrek journey!
With Love and Gratitude,
Dorianne (Band of Glow:)
Please note:
KD pic is for inspiration only - please do not use it on the site. Thank you.

Industry/Entity Type

Paint

Requirements
Must have
• Opt in for Future Newsletter, blog, vlog, join the movement - permission to get creative ;)
Email: dorianne@glowtrek.example

```html
<!DOCTYPE html>
<html lang="en">
<head>
<meta charset="utf-8">
<title>Glowtrek</title>
<link rel="stylesheet" href="https://fonts.googleapis.com/css2?family=Open+Sans:wght@400;600;700&family=Philosopher:wght@700&display=swap">
<style>
:root{
  --black:#0b0b0b;
  --red:#e3212a;
  --red-dark:#c4161e;
  --page:#ffffff;
  --text:#6b6b6b;
  --line:#dddddd;
  --bar:#f1f1f1;
  --yellow:#f4e11c;
  --blue:#2b6cb0;
}
*{box-sizing:border-box;margin:0;padding:0}
html,body{width:841px;height:1200px;overflow:hidden}
body{background:var(--page);font-family:"Open Sans",Arial,sans-serif;color:var(--text);font-size:9px;line-height:1.45;position:relative}
.site-header{height:84px;background:var(--black);display:flex;align-items:center;justify-content:space-between;padding:0 28px 0 34px}
.brand{display:flex;align-items:center;gap:8px;color:#fff;font-family:"Philosopher",Georgia,serif;font-size:30px;font-weight:700;letter-spacing:1px}
.brand-dot{width:16px;height:16px;border-radius:50%;background:var(--red)}
.main-nav{display:flex;gap:4px;align-self:flex-start;margin-top:26px}
.main-nav a{color:#fff;text-decoration:none;font-size:9.5px;padding:8px 12px}
.main-nav a.active{background:var(--red)}
.hero{position:relative;height:308px;background:linear-gradient(100deg,#2d2a26 0%,#6f6a5d 30%,#b8a57f 55%,#d48a3c 75%,#7b5f3b 100%)}
.hero-text{position:absolute;left:62px;top:104px;width:430px;color:#fff;font-size:15px;line-height:1.3;font-weight:600;text-shadow:0 1px 2px rgba(0,0,0,.6)}
.hero-arrow{position:absolute;top:138px;width:18px;height:30px}
.hero-arrow.prev{left:12px}.hero-arrow.next{right:12px}
.hero-dots{position:absolute;left:50%;bottom:12px;transform:translateX(-50%);display:flex;gap:5px}
.hero-dots span{width:6px;height:6px;border-radius:50%;background:rgba(255,255,255,.6)}
.hero-dots span.on{background:#fff}
.container{position:absolute;left:67px;width:746px}
.heading{font-family:"Philosopher",Georgia,serif;color:var(--red);font-size:21px;font-weight:700;line-height:1}
.welcome{top:412px;display:flex;gap:30px}
.welcome-copy{width:490px}
.welcome-copy p{margin-top:12px}
.newsletter{width:226px;height:188px;background:var(--red);margin-top:-12px;padding:0 14px}
.newsletter-tab{display:inline-block;background:#d9d9d9;color:#fff;background:#e9575d;font-size:10px;padding:8px 12px;margin-left:-14px}
.newsletter input{display:block;width:100%;height:22px;margin-top:12px;border:0;padding:0 8px;font-family:inherit;font-size:8px;color:#888}
.newsletter button{display:block;margin:14px 10px 0 auto;width:52px;height:22px;border:0;background:var(--yellow);font-family:inherit;font-size:8px;color:#333}
.blog{top:622px}
.blog-head{display:flex;justify-content:space-between;align-items:center}
.blog-nav{display:flex;gap:4px}
.cards{display:flex;gap:14px;margin-top:14px}
.card{flex:1;border:1px solid var(--line);height:254px;display:flex;flex-direction:column}
.card-body{display:flex;gap:12px;padding:8px;flex:1}
.card-photo{width:160px;height:192px;background:linear-gradient(160deg,#7fb3d8,#e9e2d2 45%,#d8602a 70%,#5d5140)}
.card-title{color:var(--red);font-weight:700;font-size:9.5px}
.card-text p{margin-top:4px;font-size:8px}
.card-bar{display:flex;justify-content:space-around;background:var(--bar);border-top:1px solid var(--line);height:34px;align-items:center;font-size:8px;color:#555}
.card-bar span{display:flex;align-items:center;gap:4px}
.card-bar i{width:9px;height:7px;background:var(--blue);display:inline-block;border-radius:1px}
.media{top:950px;display:flex;gap:18px}
.media-col{flex:1}
.grid{display:grid;grid-template-columns:repeat(3,1fr);gap:6px;margin-top:14px}
.thumb{height:58px;position:relative}
.thumb.a{background:linear-gradient(135deg,#e6c33a,#8a8f5a)}
.thumb.b{background:linear-gradient(135deg,#c9d6db,#e9a33b)}
.thumb.c{background:linear-gradient(135deg,#6a8f4f,#d8c98f)}
.thumb.d{background:linear-gradient(135deg,#c02a2a,#e6d6b8)}
.thumb.e{background:linear-gradient(135deg,#5c8ab8,#e5e0d5)}
.thumb.f{background:linear-gradient(135deg,#a83a3a,#f0c9a0)}
.play{position:absolute;left:50%;top:50%;width:20px;height:20px;margin:-10px 0 0 -10px}
.site-footer{position:absolute;top:1120px;left:0;width:841px;height:80px;background:var(--black);color:#fff;padding:20px 67px;font-size:8px}
.footer-links{display:flex;gap:5px}
.footer-copy{margin-top:6px;color:#ccc}
.social{position:absolute;right:50px;top:22px;display:flex;gap:3px;align-items:center}
.social span{width:14px;height:14px;background:#3b5998}
.social span:nth-child(2){background:#1da1f2}
.social span:nth-child(3){background:#dd4b39}
.social span:nth-child(4){background:#0e76a8}
.social em{font-style:normal;margin-left:8px;color:#aaa}
</style>
</head>
<body>
<header class="site-header">
  <div class="brand"><span>Glowtrek</span><span class="brand-dot"></span></div>
  <nav class="main-nav">
    <a class="active" href="#">Home</a><a href="#">About us</a><a href="#">Photo Gallery</a><a href="#">Video</a><a href="#">Blog</a><a href="#">Contact Us</a>
  </nav>
</header>

<section class="hero" role="img" aria-label="Photo of a classic camper van parked on a narrow street">
  <p class="hero-text">We are going to have a road trip in our van which is an old 1977 kd motor van.<br>We will have custom bumper stickers available, so whoever donates on our journey will get the stickers.</p>
  <svg class="hero-arrow prev" viewBox="0 0 18 30"><path d="M14 4 4 15l10 11" fill="none" stroke="#fff" stroke-width="4"/></svg>
  <svg class="hero-arrow next" viewBox="0 0 18 30"><path d="M4 4l10 11L4 26" fill="none" stroke="#fff" stroke-width="4"/></svg>
  <div class="hero-dots"><span class="on"></span><span></span><span></span></div>
</section>

<section class="container welcome">
  <div class="welcome-copy">
    <h1 class="heading">Welcome To Glowtrek</h1>
    <p>Lorem ipsum dolor sit amet, consectetuer adipiscing elit, sed diam nonummy nibh euismod tincidunt ut laoreet dolore magna aliquam erat volutpat. Ut wisi enim ad minim veniam, quis nostrud exerci tation ullamcorper suscipit lobortis nisl ut aliquip ex ea commodo consequat. Lorem ipsum dolor sit amet, consectetuer adipiscing elit, sed diam nonummy nibh euismod tincidunt ut laoreet dolore magna aliquam erat volutpat. Ut wisi enim ad minim veniam.</p>
  </div>
  <form class="newsletter">
    <span class="newsletter-tab">Newsletters</span>
    <input type="text" placeholder="Your name">
    <input type="email" placeholder="Email">
    <button type="button">Send</button>
  </form>
</section>

<section class="container blog">
  <div class="blog-head">
    <h2 class="heading">Blog</h2>
    <div class="blog-nav">
      <svg width="8" height="10" viewBox="0 0 8 10"><path d="M7 0 0 5l7 5z" fill="#333"/></svg>
      <svg width="8" height="10" viewBox="0 0 8 10"><path d="M1 0l7 5-7 5z" fill="#333"/></svg>
    </div>
  </div>
  <div class="cards">
    <article class="card">
      <div class="card-body">
        <div class="card-photo" role="img" aria-label="Photo of an orange camper van on a beach"></div>
        <div class="card-text">
          <h3 class="card-title">Lorem ipsum dolor sit amet</h3>
          <p>Lorem ipsum dolor sit amet, consectetuer adipiscing elit, sed diam nonummy nibh euismod tincidunt ut laoreet dolore magna aliquam erat volutpat.</p>
          <p>Ut wisi enim ad minim veniam, quis nostrud exerci tation ullamcorper suscipit lobortis nisl ut aliquip ex ea commodo.</p>
        </div>
      </div>
      <div class="card-bar"><span><i></i>Email Friends</span><span><i></i>Print</span><span><i></i>Comments</span><span><i></i>Like</span></div>
    </article>
    <article class="card">
      <div class="card-body">
        <div class="card-photo" role="img" aria-label="Photo of a red and white camper van on a coastal road"></div>
        <div class="card-text">
          <h3 class="card-title">Lorem ipsum dolor sit amet</h3>
          <p>Lorem ipsum dolor sit amet, consectetuer adipiscing elit, sed diam nonummy nibh euismod tincidunt ut laoreet dolore magna aliquam erat volutpat.</p>
          <p>Ut wisi enim ad minim veniam, quis nostrud exerci tation ullamcorper suscipit lobortis nisl ut aliquip ex ea commodo.</p>
        </div>
      </div>
      <div class="card-bar"><span><i></i>Email Friends</span><span><i></i>Print</span><span><i></i>Comments</span><span><i></i>Like</span></div>
    </article>
  </div>
</section>

<section class="container media">
  <div class="media-col">
    <h2 class="heading">Photo Gallery</h2>
    <div class="grid">
      <div class="thumb a" role="img" aria-label="Yellow camper van photo"></div>
      <div class="thumb b" role="img" aria-label="Camper van by the sea photo"></div>
      <div class="thumb c" role="img" aria-label="Green camper van photo"></div>
      <div class="thumb d" role="img" aria-label="Red camper van photo"></div>
      <div class="thumb e" role="img" aria-label="Blue camper van photo"></div>
      <div class="thumb f" role="img" aria-label="Camper van interior photo"></div>
    </div>
  </div>
  <div class="media-col">
    <h2 class="heading">Video</h2>
    <div class="grid">
      <div class="thumb e" role="img" aria-label="Road trip video still"><svg class="play" viewBox="0 0 20 20"><circle cx="10" cy="10" r="10" fill="#e3212a"/><path d="M8 6v8l6-4z" fill="#fff"/></svg></div>
      <div class="thumb b" role="img" aria-label="Road trip video still"><svg class="play" viewBox="0 0 20 20"><circle cx="10" cy="10" r="10" fill="#e3212a"/><path d="M8 6v8l6-4z" fill="#fff"/></svg></div>
      <div class="thumb a" role="img" aria-label="Road trip video still"><svg class="play" viewBox="0 0 20 20"><circle cx="10" cy="10" r="10" fill="#e3212a"/><path d="M8 6v8l6-4z" fill="#fff"/></svg></div>
      <div class="thumb d" role="img" aria-label="Road trip video still"><svg class="play" viewBox="0 0 20 20"><circle cx="10" cy="10" r="10" fill="#e3212a"/><path d="M8 6v8l6-4z" fill="#fff"/></svg></div>
      <div class="thumb c" role="img" aria-label="Road trip video still"><svg class="play" viewBox="0 0 20 20"><circle cx="10" cy="10" r="10" fill="#e3212a"/><path d="M8 6v8l6-4z" fill="#fff"/></svg></div>
      <div class="thumb f" role="img" aria-label="Road trip video still"><svg class="play" viewBox="0 0 20 20"><circle cx="10" cy="10" r="10" fill="#e3212a"/><path d="M8 6v8l6-4z" fill="#fff"/></svg></div>
    </div>
  </div>
</section>

<footer class="site-footer">
  <div class="footer-links"><span>Home</span>|<span>About</span>|<span>Practices</span>|<span>People</span>|<span>Events</span>|<span>Contact</span>|<span>Site Map</span>|<span>Privacy Policy</span></div>
  <p class="footer-copy">© 2014 Glowtrek . All rights reserved.</p>
  <div class="social"><span></span><span></span><span></span><span></span><em>top</em></div>
</footer>
</body>
</html>
```